Beauty Salon @ Medspa ,
Verdant Glow Skin Care
Project: Beauty Salon @ Medspa ,
Beauty Salon @ Medspa ,  - Salon & Spa
Creative Brief
Professional
Lorna Yeo Mei Ling
President of Verdant Glow Corporation 사장
Lot 5.12 , 2nd Floor Selindung Plaza 7700 , Kota Kinabalu ,Sabah, East Malaysia
lorna@verdantglow-example.co.kr
www.verdantglow-example.co.kr
I'll be using Hotstamping and UV to printing for the namecard , I want some creative design.
Logo and website will be great
torefelo torefelo
Cell : +6019 4271935 and the Tel have a +6 088 as well , thanks .

```html
<!DOCTYPE html>
<html lang="en">
<head>
<meta charset="utf-8">
<title>Verdant Glow Skin Care – Business Card</title>
<link rel="stylesheet" href="https://fonts.googleapis.com/css2?family=Open+Sans:wght@400;600;700&display=swap">
<style>
  :root {
    --stage: #3a3a3c;
    --card-white: #fbfbfb;
    --brand-purple: #7b3394;
    --purple-deep: #6a2880;
    --purple-light: #8d45a6;
    --leaf-green: #3f7a1f;
    --leaf-dark: #2c5a14;
    --leaf-light: #6ea33b;
    --text-grey: #6b6b6b;
    --icon-grey: #8a8a8a;
  }
  * { margin: 0; padding: 0; box-sizing: border-box; }
  html, body {
    width: 1200px; height: 751px; overflow: hidden;
    background: var(--stage);
    font-family: "Open Sans", Arial, sans-serif;
  }
  .stage { position: relative; width: 1200px; height: 751px; }
  .card {
    position: absolute; top: 216px;
    width: 492px; height: 288px; border-radius: 14px; overflow: hidden;
  }
  .card--front { left: 91px; background: var(--card-white); }
  .card--back {
    left: 619px;
    background: radial-gradient(ellipse at 50% 45%, var(--purple-light), var(--brand-purple) 55%, var(--purple-deep));
  }
  .swoosh { position: absolute; inset: 0; width: 492px; height: 288px; }
  .brand-name {
    position: absolute; color: var(--brand-purple);
    font-weight: 600; line-height: 1.05; letter-spacing: 0.5px;
  }
  .card--front .brand-name { left: 30px; top: 30px; font-size: 30px; }
  .brand-name .mark {
    display: inline-block; width: 12px; height: 12px; border-radius: 50%;
    background: currentColor; margin-left: 6px; vertical-align: middle;
  }
  .card--back .brand-name {
    left: 0; right: 0; top: 104px; text-align: center;
    color: #fff; font-size: 32px;
  }
  .holder { position: absolute; left: 30px; top: 150px; }
  .holder-name { color: var(--brand-purple); font-weight: 700; font-size: 18px; }
  .holder-title { color: var(--text-grey); font-size: 12px; margin-top: 2px; }
  .address {
    position: absolute; left: 30px; top: 204px;
    color: var(--text-grey); font-size: 11px; line-height: 17px;
  }
  .contacts {
    position: absolute; left: 178px; top: 202px; list-style: none;
    color: var(--text-grey); font-size: 11px; line-height: 17.5px;
  }
  .contacts li { display: flex; align-items: center; gap: 8px; }
  .contacts svg { width: 11px; height: 11px; fill: var(--icon-grey); flex: none; }
</style>
</head>
<body>
<main class="stage">
  <section class="card card--front" aria-label="Business card front">
    <svg class="swoosh" viewBox="0 0 492 288" aria-hidden="true">
      <defs>
        <linearGradient id="leafFill" x1="0" y1="0" x2="1" y2="1">
          <stop offset="0" stop-color="var(--leaf-light)"/>
          <stop offset="0.45" stop-color="var(--leaf-green)"/>
          <stop offset="1" stop-color="var(--leaf-dark)"/>
        </linearGradient>
      </defs>
      <path d="M300 0 C410 25 440 150 452 288 H492 V0 Z" fill="url(#leafFill)"/>
      <path d="M355 0 C420 20 470 70 492 118" fill="none" stroke="#fff" stroke-width="9"/>
    </svg>

    <div class="brand-name">Verdant Glow<span class="mark"></span><br>Skin Care</div>

    <div class="holder">
      <p class="holder-name">Lorna Yeo Mei Ling</p>
      <p class="holder-title">President</p>
    </div>

    <p class="address">Lot 5.12 , 2nd Floor<br>Selindung Plaza<br>7700 , Kota Kinabalu<br>Sabah, East Malaysia</p>

    <ul class="contacts">
      <li><svg viewBox="0 0 12 12"><rect x="0" y="3" width="12" height="8" rx="1.5"/><rect x="2" y="0" width="8" height="3" rx="1"/></svg>+6088 5129043</li>
      <li><svg viewBox="0 0 12 12"><rect x="2.5" y="0" width="7" height="12" rx="1.5"/></svg>+6019 4271935</li>
      <li><svg viewBox="0 0 12 12"><rect x="0" y="2" width="12" height="8" rx="1"/></svg>lorna@verdantglow-example.co.kr</li>
      <li><svg viewBox="0 0 12 12"><circle cx="6" cy="6" r="6"/></svg>www.verdantglow-example.co.kr</li>
    </ul>
  </section>

  <section class="card card--back" aria-label="Business card back">
    <div class="brand-name">Verdant Glow<br>Skin Care</div>
  </section>
</main>
</body>
</html>
```